Wohlauf im Wandel
Zielgruppe
Ich biete einen print Informationsdienst an. Name: Wohlauf im Wandel Untertitel: Ihre leichtverständliche Gebrauchsanweisung für den sicheren Umgang mit Technik im Alltag.
Zielgruppe sind Senioren, Rentner und 'ältere Menschen' ab 55+. Denen sollen technische Neuerungen in leichtverständlicher Sprache und Schritt für Schritt erklärt werden. Wie funktionieren digatale Überwachungskameras? Welche Möglichkeiten habe ich mit meinem Smartphone? Wie gut sind Staubsaugerroboter? etc.
Die Zielgruppe will Technik für sich nutzen, aber nur dann wenn sie sinnvoll und alltagstauglich ist. Ich möchte die Frage klären: 'Was bringt mir denn der ganze neumodische Schnickschnack?'.
Die Leser von 'Wohlauf im Wandel' wollen einfache Auskünfte und keine überkandidelte (englische) Sprache. Neue Geräte sollen ihren Preis wert sein und keine nutzlosen Spielerein sein.
Pro Monat erscheint einmal ein Heft, indem über technische Neuerungen und der Gebrauch mit ihnen informiert wird. Auch werden relevante Testergebnisse und Sicherheitshinweise veröffentlicht.
Aufgabenstellung
Ich brauche einen Header für meine Zeitschrift.
Titel: Wohlauf im Wandel
Untertitel: Ihre leichtverständliche Gebrauchsanweisung für den sicheren Umgang mit Technik im Alltag
Größe 4,80 cm höhe, 20,8 breit (die Höhe kann auch etwas (!) größer sein, die Breite ist unveränderbar!)
Farbgestaltung ist nicht vorgegeben, es muss Platz für eine Ausgabennummer (meist Monat + Jahr (also März 2016)) sein und die Zielgruppe berücksichtigen.
Der Standard bei uns im Haus ist eine farbige Vollfläche in obengenannter Größe und darauf dann entsprechend Schrift (Titel), Abbildungen, Störer, Stempel oder was auch immer (inhaltlich zum Thema) passt.

```html
<!DOCTYPE html>
<html lang="de">
<head>
<meta charset="utf-8">
<title>Wohlauf im Wandel – Header-Varianten</title>
<link href="https://fonts.googleapis.com/css2?family=Open+Sans:wght@400;700;800&display=swap" rel="stylesheet">
<style>
  :root {
    --gold: #e0a830;
    --navy: #243f5f;
    --red: #c33b2e;
    --blue: #3374bb;
    --berry: #a83354;
    --salmon: #e0836a;
    --white: #ffffff;
    --cream: #fbf8ee;
  }
  html, body {
    margin: 0;
    padding: 0;
    width: 963px;
    height: 1200px;
    overflow: hidden;
    background: var(--white);
    font-family: "Open Sans", Arial, sans-serif;
  }
  .canvas {
    position: relative;
    width: 963px;
    height: 1200px;
  }
  .header {
    position: absolute;
    left: 61px;
    width: 839px;
    height: 191px;
    border-bottom: 4px solid var(--navy);
    overflow: hidden;
  }
  .header--gold  { top: 47px;  background: var(--gold); }
  .header--red   { top: 272px; background: var(--red); }
  .header--blue  { top: 501px; background: var(--blue); }
  .header--berry { top: 729px; background: var(--berry); }
  .header--navy  { top: 957px; background: var(--navy); }

  .header__title {
    position: absolute;
    left: 43px;
    top: 32px;
    margin: 0;
    font-weight: 800;
    font-size: 49px;
    line-height: 1;
    letter-spacing: 0.5px;
    text-transform: uppercase;
    white-space: nowrap;
  }
  .header__subtitle {
    position: absolute;
    left: 43px;
    top: 88px;
    margin: 0;
    font-weight: 700;
    font-size: 22px;
    line-height: 28px;
    letter-spacing: 0.6px;
    color: var(--white);
    white-space: nowrap;
  }
  .header__issue {
    position: absolute;
    left: 43px;
    top: 171px;
    margin: 0;
    font-weight: 400;
    font-size: 14px;
    line-height: 18px;
    color: var(--white);
    text-transform: uppercase;
  }
  .header--gold .header__title,
  .header--gold .header__issue { color: var(--navy); }
  .header--red .header__title,
  .header--blue .header__title,
  .header--berry .header__title { color: var(--gold); }
  .header--navy .header__title { color: var(--salmon); }

  .header__visual {
    position: absolute;
    right: 0;
    top: 0;
    width: 194px;
    height: 191px;
  }
  .header--gold .header__visual  { background: var(--cream); }
  .header--red .header__visual   { background: linear-gradient(160deg, #7d6a4a 0%, #d8c6b2 45%, #e0553a 75%, #c9c4c0 100%); }
  .header--blue .header__visual  { background: linear-gradient(135deg, #e3e6ea 0%, #c9b5a3 40%, #b8d7cf 75%, #dfe3e6 100%); }
  .header--berry .header__visual { background: linear-gradient(135deg, #d9e8ec 0%, #e3c5a5 35%, #9e3a48 65%, #d6d0c4 100%); }
  .header--navy .header__visual  { background: linear-gradient(135deg, #c5c9cc 0%, #5a6f8a 40%, #a85a3e 70%, #d9d4cd 100%); }
</style>
</head>
<body>
<div class="canvas">

  <section class="header header--gold">
    <h1 class="header__title">Wohlauf im Wandel</h1>
    <p class="header__subtitle">Ihre leichtverständliche Gebrauchsanweisung<br>für den sicheren Umgang mit Technik im Alltag</p>
    <p class="header__issue">März 2016</p>
    <div class="header__visual" role="img" aria-label="Raster aus Linien-Symbolen von Haushaltsgeräten wie Waschmaschine, Kühlschrank, Wasserkocher, Bügeleisen und Telefon"></div>
  </section>

  <section class="header header--red">
    <h1 class="header__title">Wohlauf im Wandel</h1>
    <p class="header__subtitle">Ihre leichtverständliche Gebrauchsanweisung<br>für den sicheren Umgang mit Technik im Alltag</p>
    <p class="header__issue">März 2016</p>
    <div class="header__visual" role="img" aria-label="Foto: lachende ältere Frau mit Brille fotografiert mit einer roten Kamera"></div>
  </section>

  <section class="header header--blue">
    <h1 class="header__title">Wohlauf im Wandel</h1>
    <p class="header__subtitle">Ihre leichtverständliche Gebrauchsanweisung<br>für den sicheren Umgang mit Technik im Alltag</p>
    <p class="header__issue">März 2016</p>
    <div class="header__visual" role="img" aria-label="Foto: älteres Paar auf dem Sofa mit Fernbedienung"></div>
  </section>

  <section class="header header--berry">
    <h1 class="header__title">Wohlauf im Wandel</h1>
    <p class="header__subtitle">Ihre leichtverständliche Gebrauchsanweisung<br>für den sicheren Umgang mit Technik im Alltag</p>
    <p class="header__issue">März 2016</p>
    <div class="header__visual" role="img" aria-label="Foto: älteres Paar spielt lachend Videospiele mit Controllern"></div>
  </section>

  <section class="header header--navy">
    <h1 class="header__title">Wohlauf im Wandel</h1>
    <p class="header__subtitle">Ihre leichtverständliche Gebrauchsanweisung<br>für den sicheren Umgang mit Technik im Alltag</p>
    <p class="header__issue">März 2016</p>
    <div class="header__visual" role="img" aria-label="Foto: älterer Mann montiert eine Gegensprechanlage an einer Backsteinmauer"></div>
  </section>

</div>
</body>
</html>
```